Wellness, Purpose, and the Quiet Path Research Program Website

Overview: This website will serve a new research program (Wellness, Purpose, and the Quiet Path) at the Thornbury University School of Medicine. I want a clean, intuitive design that has a navigation bar, but uses icons/graphic buttons to link to the main pages. In an attached Word document, I have provided a basic information architecture for the site, understanding that this project would just generate graphics and code for the 3 pages. I highlighted the 3 pages I'd like designed.
Target market: People who want to participate in our research, or contribute grant funding to specific projects.
Number of page: The design project focuses on 3 pages, but the site must accommodate 6 pages with top-level links. See attached Word doc.
Logo and website header: Please integrate our logo in the header. I've uploaded it as a png file--both with the name of the website and with just the logo image. I imaging the logo would look great in a banner set against an image of a mountain. The two main design themes I want to see included are nature and healthcare.
Text content: I have not yet provided text. Use some dummy text.
Technical Specifications:
- Build using WordPress. We will host this site ourselves on HostBarrow using WordPress.
- The design package must be coded.
- The template must be responsive to different platforms (e.g., computer, mobile phone, Zelvo).
Thank you! I look forward to seeing your designs.
- Ned

```html
<!DOCTYPE html>
<html lang="en">
<head>
<meta charset="utf-8">
<title>Wellness, Purpose, and the Quiet Path Research Program</title>
<link href="https://fonts.googleapis.com/css2?family=Poppins:wght@300;400;500;600;700&display=swap" rel="stylesheet">
<style>
:root{
  --teal:#12a88b;
  --blue:#1670b8;
  --blue-deep:#0f5ea6;
  --blue-soft:#7ca8d7;
  --navy:#1f2733;
  --navy-2:#1a222d;
  --ink:#1d2430;
  --muted:#5d6673;
  --mist:#eef3f7;
  --white:#ffffff;
}
*{box-sizing:border-box;margin:0;padding:0}
html,body{width:1200px;height:1200px;overflow:hidden;background:var(--white)}
body{font-family:"Poppins",sans-serif;color:var(--ink);position:relative}
.page{position:absolute;left:473px;top:32px;width:1920px;height:8561px;transform:scale(0.1328);transform-origin:0 0;background:var(--white);overflow:hidden}
.abs{position:absolute}
.ph{position:absolute}
p{font-size:19px;line-height:1.6;color:var(--muted)}
.btn{position:absolute;background:var(--teal);color:#fff;font-size:17px;font-weight:500;letter-spacing:1px;padding:12px 22px;text-transform:uppercase}
.h2{font-size:52px;font-weight:400;line-height:1.2;color:var(--ink)}
.h2 b{font-weight:600;color:var(--blue-deep)}

/* hero */
.hero-photo{position:absolute;left:0;top:0;width:1920px;height:1082px;clip-path:polygon(0 0,100% 0,100% 1026px,0 1082px);
  background:
    radial-gradient(circle at 72% 24%,rgba(255,252,236,.98) 0,rgba(255,238,196,.7) 8%,rgba(255,230,180,0) 28%),
    radial-gradient(ellipse 30% 45% at 90% 78%,#33361f 0,#4d4a2b 40%,rgba(77,74,43,0) 100%),
    radial-gradient(ellipse 22% 40% at 82% 55%,rgba(70,70,40,.85) 0,rgba(70,70,40,0) 100%),
    radial-gradient(ellipse 28% 22% at 14% 98%,#2a251b 0,#4a4030 50%,rgba(74,64,48,0) 100%),
    radial-gradient(ellipse 50% 12% at 40% 62%,rgba(250,244,228,.8) 0,rgba(250,244,228,0) 100%),
    linear-gradient(180deg,#cbd6da 0%,#e6e2d2 22%,#ecdcb8 38%,#dcc8a0 50%,#b3a07c 62%,#7b6d4d 78%,#45402c 100%)}
.hero-band{position:absolute;left:0;top:0;width:1920px;height:1082px;clip-path:polygon(1260px 950px,1920px 876px,1920px 1026px);background:var(--teal)}
.brand{position:absolute;left:276px;top:58px;display:flex;align-items:center;gap:14px}
.brand i{width:64px;height:64px;border-radius:50%;background:var(--blue);display:block}
.brand .bt{font-size:15px;font-weight:600;color:var(--blue-deep);width:390px;line-height:1.3}
.brand .bt small{display:block;font-size:15px;font-weight:600;color:var(--teal)}
.nav{position:absolute;right:276px;top:74px;display:flex;gap:46px;font-size:19px;color:#2a3340}
.nav span::before{content:"";display:inline-block;width:14px;height:14px;border-radius:50%;background:#3a4450;margin-right:8px;vertical-align:-1px}
.nav .on{color:var(--teal)}
.nav .on::before{background:var(--teal)}
.hero-title{position:absolute;left:0;width:1920px;top:360px;text-align:center;font-size:74px;font-weight:600;color:var(--navy);letter-spacing:1px}
.hero-sub{position:absolute;left:0;width:1920px;top:450px;text-align:center;font-size:30px;letter-spacing:3px;color:#2b2f36}
.hero-btn{left:860px;top:540px;background:var(--blue);font-size:19px;padding:16px 28px}

/* welcome */
.welcome-h{position:absolute;left:276px;top:1235px}
.welcome-p{position:absolute;left:276px;width:660px;font-size:18px}

/* projects */
.projects{position:absolute;left:0;top:1995px;width:1920px;height:1367px;background:var(--mist)}
.tri{position:absolute;left:0;top:1967px;width:1920px;height:260px;clip-path:polygon(0 0,876px 131px,0 239px);background:var(--blue-soft)}
.tri-w{position:absolute;left:0;top:1967px;width:1920px;height:300px;clip-path:polygon(876px 131px,1920px 28px,1920px 0,0 0);background:var(--white)}
.center-h{position:absolute;left:0;width:1920px;text-align:center}
.center-p{position:absolute;left:460px;width:1000px;text-align:center;font-size:18px}
.card-blue{position:absolute;left:951px;top:2964px;width:576px;height:267px;background:var(--blue);padding:36px 50px;color:#fff}
.card-blue h4{font-size:27px;font-weight:500;margin-bottom:12px}
.card-blue p{color:#dce9f6;font-size:17px}
.card-blue u{display:block;margin-top:14px;font-size:15px;font-weight:600}
.arrows{position:absolute;left:417px;top:3192px;width:140px;height:52px;background:#fff;display:flex;align-items:center;justify-content:space-around;font-size:26px;color:var(--ink)}

/* resources */
.res-h{position:absolute;left:276px;top:3610px}
.rc{position:absolute;width:431px;height:497px;color:#fff;overflow:hidden}
.rc .ph{inset:0}
.rc::after{content:"";position:absolute;left:0;right:0;bottom:0;height:55%;background:linear-gradient(180deg,rgba(22,90,160,0),rgba(22,90,160,.75))}
.rc .cap{position:absolute;left:26px;bottom:26px;right:26px;z-index:1}
.rc h5{font-size:20px;font-weight:500;margin-bottom:8px}
.rc p{color:#e6eef6;font-size:15px;line-height:1.5}

/* faq */
.faq-l{position:absolute;left:0;top:4927px;width:684px;height:1081px;background:var(--teal)}
.faq-r{position:absolute;left:684px;top:4927px;width:1236px;height:1081px;background:var(--navy)}
.frame{position:absolute;left:278px;top:5042px;width:670px;height:826px;border:4px solid var(--blue)}
.faq-h{position:absolute;left:1026px;top:5100px;font-size:50px;font-weight:400;color:#fff;line-height:1.2}
.faq-h b{color:#3c98e0;font-weight:600}
.q{position:absolute;left:1026px;width:630px;font-size:20px;color:#fff;border-bottom:1px solid #3b4654;padding-bottom:18px;padding-right:30px}
.q em{font-style:normal;color:#3c98e0;margin-right:6px}
.q::after{content:"+";position:absolute;right:0;top:0;color:#cfd6de}
.q.open::after{content:"–"}

/* team */
.tm{position:absolute;width:314px;height:398px;background:#fff;border:2px solid #e6eaef;text-align:center}
.tm .ph{left:14px;top:14px;width:282px;height:296px}
.tm span{position:absolute;left:0;right:0;bottom:22px;font-size:21px}
.tm.on{border-color:#9cc2e6;box-shadow:0 8px 24px rgba(22,112,184,.15)}
.tm.on span{color:var(--blue)}

/* footer */
.footer{position:absolute;left:0;top:7886px;width:1920px;height:675px;background:var(--navy)}
.footer .bar{position:absolute;left:0;bottom:0;width:1920px;height:74px;background:var(--navy-2);text-align:center;font-size:15px;color:#a8b0ba;line-height:74px}
.footer .bar b{color:var(--teal);font-weight:400}
.partners{position:absolute;left:276px;top:7821px;width:1368px;height:150px;background:#fff;display:flex;align-items:center;justify-content:space-around;padding:0 40px}
.partners i{display:block;background:#c9ced5}
.fcol{position:absolute;top:8080px;font-size:16px;color:#c9d0d8;line-height:40px}
.fcol h6{font-size:19px;font-weight:500;color:#fff;margin-bottom:10px;line-height:1.4}
.fcol h6 b{color:var(--teal);font-weight:400}
.fcol .lab{color:var(--teal);font-size:14px;line-height:1.5}
.fcol .val{line-height:1.5;margin-bottom:12px}
.f-about{left:276px;width:420px;line-height:1.5;top:8100px}
.f-brand{display:flex;gap:12px;align-items:center;margin-bottom:16px}
.f-brand i{width:56px;height:56px;border-radius:50%;background:var(--blue);display:block}
.f-brand span{color:#fff;font-size:14px;font-weight:600;width:320px}
.soc{display:flex;gap:10px;margin-top:14px}
.soc i{width:30px;height:30px;border-radius:50%;border:2px solid #c9d0d8;display:block}
</style>
</head>
<body>
<div class="page">

  <!-- hero -->
  <div class="hero-photo" role="img" aria-label="Hiker on a rocky summit above misty mountains at sunrise"></div>
  <div class="hero-band"></div>
  <div class="brand"><i></i><div class="bt">Wellness, Purpose, and the Quiet Path<small>Research Program</small></div></div>
  <nav class="nav"><span class="on">Home</span><span>People</span><span>Projects</span><span>FAQ</span><span>Resource</span><span>Contact</span></nav>
  <h1 class="hero-title">TRATMENT THAT WORKS</h1>
  <div class="hero-sub">PERSONAL CARE PERSONAL RECOVERY</div>
  <div class="btn hero-btn">Contact Us</div>

  <!-- welcome -->
  <h2 class="h2 welcome-h">Welcome To<br><b>WPQ Research Program</b></h2>
  <p class="welcome-p" style="top:1375px">Lorem ipsum dolor sit amet, consectetur adipiscing elit. Curabitur nisl risus, rutrum ac consectetur eu, accumsan eget nibh. Vivamus placerat a lacus ac aliquam. Vestibulum porttitor erat at dui gravida tempor. Quisque semper faucibus ipsum, non gravida erat fermentum vitae.</p>
  <p class="welcome-p" style="top:1535px">Aenean blandit mattis pulvinar. Aliquam interdum tempor ultricies. Cras eget pharetra erat. Vivamus molestie feugiat leo vel sollicitudin tortor. Ut interdum arcu vel vehicula laoreet. Donec est nulla, porttitor a sapien eget, facilisis ullamcorper libero. Sed at tincidunt ante. Donec imperdiet massa id elit consectetur, sit amet facilisis dui pulvinar.</p>
  <div class="btn" style="left:276px;top:1730px;font-size:15px;padding:10px 18px">Learn More</div>
  <div class="ph" style="left:1000px;top:1268px;width:447px;height:530px;background:#e4ebf2"></div>
  <div class="ph" role="img" aria-label="Woman with raised arms on a coastal cliff, with a play button" style="left:1026px;top:1241px;width:421px;height:529px;background:radial-gradient(ellipse 40% 30% at 70% 90%,#6e5a40 0,rgba(110,90,64,0) 100%),linear-gradient(180deg,#cfe0ee 0%,#9fc1dc 30%,#4f84aa 50%,#3d6f8e 62%,#7b6a52 78%,#5a4a38 100%)"></div>
  <svg class="abs" style="left:1196px;top:1465px" width="80" height="80" viewBox="0 0 80 80"><circle cx="40" cy="40" r="40" fill="#1670b8"/><path d="M32 26 L56 40 L32 54Z" fill="#fff"/></svg>
  <div class="ph" role="img" aria-label="Woman breathing fresh air in a green meadow" style="left:1456px;top:1199px;width:262px;height:337px;background:linear-gradient(180deg,#a9c9e6 0%,#d4e4ef 45%,#b8cc9a 70%,#6f9a45 100%)"></div>
  <div class="ph" role="img" aria-label="Two scientists working at a microscope" style="left:1456px;top:1550px;width:324px;height:267px;background:radial-gradient(ellipse 40% 50% at 70% 40%,#ffffff 0,rgba(255,255,255,0) 100%),linear-gradient(135deg,#dfe9f3 0%,#a9c4df 50%,#3f78b0 100%)"></div>

  <!-- research projects -->
  <div class="projects"></div>
  <div class="tri-w"></div>
  <div class="tri"></div>
  <h2 class="h2 center-h" style="top:2225px">Research <b>Projects</b></h2>
  <p class="center-p" style="top:2300px">Lorem ipsum dolor sit amet, consectetur adipiscing elit. Curabitur nisl risus, rutrum ac consectetur eu, accumsan eget nibh. Vivamus placerat a lacus ac aliquam.</p>
  <div class="ph" role="img" aria-label="Pipettes and test tubes in a lab" style="left:0;top:2440px;width:356px;height:782px;background:radial-gradient(ellipse 40% 20% at 55% 70%,#c7652e 0,rgba(199,101,46,0) 100%),linear-gradient(135deg,#f1ecd6 0%,#d8cf9e 35%,#b4a86a 65%,#7a7350 100%)"></div>
  <div class="ph" role="img" aria-label="Research team working in a laboratory" style="left:393px;top:2440px;width:1134px;height:782px;background:radial-gradient(ellipse 22% 35% at 30% 30%,#eef3f8 0,rgba(238,243,248,0) 100%),radial-gradient(ellipse 20% 35% at 62% 28%,#f3f0ea 0,rgba(243,240,234,0) 100%),radial-gradient(ellipse 18% 30% at 80% 45%,#e9eef4 0,rgba(233,238,244,0) 100%),linear-gradient(180deg,#6f97bf 0%,#2f659c 55%,#1b4a7c 80%,#2d78c0 100%)"></div>
  <div class="ph" role="img" aria-label="Laboratory glassware on a bench" style="left:1564px;top:2440px;width:356px;height:782px;background:radial-gradient(ellipse 50% 30% at 60% 70%,#f5f8fb 0,rgba(245,248,251,0) 100%),linear-gradient(160deg,#2e5f96 0%,#6d98c4 45%,#cfe0ee 100%)"></div>
  <div class="card-blue"><h4>Research Organization</h4><p>Lorem ipsum dolor sit amet, consectetur adipiscing elit. Curabitur nisl risus, rutrum ac consectetur eu, accumsan eget nibh.</p><u>LEARN MORE</u></div>
  <div class="arrows"><span>←</span><span>→</span></div>

  <!-- resources -->
  <h2 class="h2 res-h">Our <b>Resources</b></h2>
  <p class="abs" style="left:276px;top:3690px;width:420px;font-size:18px">Lorem ipsum dolor sit amet, consectetur adipiscing elit. Curabitur nisl risus, rutrum ac consectetur eu, accumsan eget nibh. Vivamus placerat a lacus ac aliquam.</p>
  <div class="btn" style="left:276px;top:3830px;font-size:15px;padding:10px 18px">View More</div>
  <div class="rc" style="left:276px;top:3999px"><div class="ph" role="img" aria-label="Blue laboratory flasks" style="background:radial-gradient(ellipse 40% 30% at 40% 40%,#e6f4fb 0,rgba(230,244,251,0) 100%),linear-gradient(160deg,#bfe0f2 0%,#5fb0dc 45%,#2f7fc0 100%)"></div><div class="cap"><h5>LOREM IPSUM DOLOR</h5><p>Lorem ipsum dolor sit amet, consectetur adipiscing elit. Curabitur nisl risus, rutrum ac consectetur eu.</p></div></div>
  <div class="rc" style="left:745px;top:3695px"><div class="ph" role="img" aria-label="Man with open arms facing a mountain view" style="background:linear-gradient(180deg,#dfe4e8 0%,#c9d2da 30%,#8ea3b6 50%,#5e7f98 65%,#3f6b94 100%)"></div><div class="cap"><h5>LOREM IPSUM DOLOR</h5><p>Lorem ipsum dolor sit amet, consectetur adipiscing elit. Curabitur nisl risus, rutrum ac consectetur eu.</p></div></div>
  <div class="rc" style="left:1213px;top:3540px"><div class="ph" role="img" aria-label="Scientist working at a lab hood" style="background:radial-gradient(ellipse 35% 35% at 40% 35%,#d6dde4 0,rgba(214,221,228,0) 100%),linear-gradient(180deg,#23518e 0%,#3e74b2 50%,#2d5f9c 100%)"></div><div class="cap"><h5>LOREM IPSUM DOLOR</h5><p>Lorem ipsum dolor sit amet, consectetur adipiscing elit. Curabitur nisl risus, rutrum ac consectetur eu.</p></div></div>
  <div class="rc" style="left:745px;top:4229px"><div class="ph" role="img" aria-label="Smiling doctor talking with a patient" style="background:radial-gradient(ellipse 35% 40% at 70% 35%,#ffffff 0,rgba(255,255,255,0) 100%),linear-gradient(135deg,#7f9a86 0%,#dfe6ea 35%,#eef2f4 60%,#8fb0cf 100%)"></div><div class="cap"><h5>LOREM IPSUM DOLOR</h5><p>Lorem ipsum dolor sit amet, consectetur adipiscing elit. Curabitur nisl risus, rutrum ac consectetur eu.</p></div></div>
  <div class="rc" style="left:1213px;top:4074px"><div class="ph" role="img" aria-label="Hiker resting on a misty mountain top" style="background:radial-gradient(ellipse 15% 15% at 40% 42%,#e0b832 0,rgba(224,184,50,0) 100%),linear-gradient(180deg,#e2e9ee 0%,#b9cbd8 35%,#7f9db6 60%,#4d7aa3 100%)"></div><div class="cap"><h5>LOREM IPSUM DOLOR</h5><p>Lorem ipsum dolor sit amet, consectetur adipiscing elit. Curabitur nisl risus, rutrum ac consectetur eu.</p></div></div>

  <!-- faq -->
  <div class="faq-l"></div>
  <div class="faq-r"></div>
  <div class="frame"></div>
  <div class="ph" role="img" aria-label="Caregiver embracing a smiling elderly woman" style="left:258px;top:5062px;width:650px;height:806px;background:radial-gradient(ellipse 30% 20% at 30% 22%,#5a3f30 0,rgba(90,63,48,0) 100%),radial-gradient(ellipse 30% 22% at 62% 38%,#e9d7c4 0,rgba(233,215,196,0) 100%),radial-gradient(ellipse 45% 30% at 55% 80%,#dfe8f2 0,rgba(223,232,242,0) 100%),linear-gradient(135deg,#bfd3b2 0%,#e3d3c0 40%,#c9d9ea 75%,#9fb9d6 100%)"></div>
  <h2 class="faq-h">Frequently<br><b>Asked Questions</b></h2>
  <p class="abs" style="left:1026px;top:5250px;width:630px;color:#c5ccd5;font-size:17px">Lorem ipsum dolor sit amet, consectetur adipiscing elit. Curabitur nisl risus, rutrum ac consectetur eu, accumsan eget nibh.</p>
  <div class="q open" style="top:5345px"><em>01.</em>What makes this project unique?<p style="color:#c5ccd5;font-size:15px;margin-top:14px">Aliquam facilisis ligula a tempus congue. Aliquam lobortis est et mi accumsan suscipit. Sed iaculis, orci sed porttitor tempor, risus massa vehicula lorem, eu faucibus augue arcu sed lectus.</p></div>
  <div class="q" style="top:5535px"><em>02.</em>Does this project assume that the impact of religion is always positive?</div>
  <div class="q" style="top:5665px"><em>03.</em>How can I collaborate?</div>
  <div class="q" style="top:5758px;border:none"><em>04.</em>Will Thornbury U faculty lead all projects?</div>

  <!-- good service -->
  <h2 class="h2" style="position:absolute;left:276px;top:6290px">Good service and<br><b>better health by our<br>specialists</b></h2>
  <p class="abs" style="left:276px;top:6480px;width:600px;font-size:16px">Aliquam facilisis ligula a tempus congue. Aliquam lobortis est et mi accumsan suscipit. Sed iaculis, orci sed porttitor tempor, risus massa vehicula lorem, eu faucibus augue arcu sed lectus. Proin in rutrum nisl. Fusce aliquam lacus justo, quis ultrices nisi tristique vitae.</p>
  <div class="btn" style="left:276px;top:6665px;font-size:15px;padding:10px 18px">Contact Now</div>
  <svg class="abs" style="left:1076px;top:6220px" width="134" height="134"><path d="M134 0 A134 134 0 0 0 0 134 L134 134Z" fill="#7ca8d7"/></svg>
  <div class="ph" role="img" aria-label="Doctor portrait" style="left:1222px;top:6220px;width:124px;height:134px;background:radial-gradient(ellipse 40% 45% at 50% 60%,#ffffff 0,rgba(255,255,255,0) 100%),linear-gradient(180deg,#dfe6ee,#a9bdd2)"></div>
  <div class="ph" role="img" aria-label="Hiker on a rock above a lake" style="left:1370px;top:6220px;width:262px;height:280px;background:radial-gradient(ellipse 30% 25% at 40% 85%,#6a5a3e 0,rgba(106,90,62,0) 100%),linear-gradient(180deg,#e3edf3 0%,#b9d2e2 35%,#5f8fae 60%,#3f6c88 100%)"></div>
  <div class="ph" role="img" aria-label="Doctor checking an elderly patient" style="left:948px;top:6366px;width:408px;height:430px;background:radial-gradient(ellipse 30% 40% at 75% 50%,#6f8d63 0,rgba(111,141,99,0) 100%),radial-gradient(ellipse 35% 45% at 25% 55%,#f4f6f8 0,rgba(244,246,248,0) 100%),linear-gradient(135deg,#e6ebef 0%,#c8d4de 50%,#8ea9c3 100%)"></div>
  <div class="ph" role="img" aria-label="Medical staff" style="left:1370px;top:6516px;width:124px;height:130px;background:linear-gradient(180deg,#eef2f6,#b7c8da)"></div>
  <svg class="abs" style="left:1508px;top:6516px" width="134" height="130"><path d="M134 0 L0 0 L0 130 A134 130 0 0 0 134 0Z" fill="#6fd6c4"/></svg>
  <div class="ph" role="img" aria-label="Doctors in consultation" style="left:1370px;top:6660px;width:272px;height:136px;background:linear-gradient(90deg,#e1e7ee,#f4f6f8 50%,#c3d2e1)"></div>

  <!-- team -->
  <h2 class="h2 center-h" style="top:6955px">Meet <b>Our Team</b></h2>
  <p class="center-p" style="top:7030px">Lorem ipsum dolor sit amet, consectetur adipiscing elit. Curabitur nisl risus, rutrum ac consectetur eu, accumsan eget nibh. Vivamus placerat a lacus ac aliquam.</p>
  <div class="tm" style="left:276px;top:7170px"><div class="ph" role="img" aria-label="Team member portrait" style="background:radial-gradient(ellipse 45% 40% at 50% 80%,#f5f7f9 0,rgba(245,247,249,0) 100%),linear-gradient(180deg,#e9eff5 0%,#b8cde2 60%,#5b89b8 100%)"></div><span>Marcus Treval</span></div>
  <div class="tm on" style="left:627px;top:7148px"><div class="ph" role="img" aria-label="Team member portrait" style="background:radial-gradient(ellipse 40% 45% at 50% 78%,#ffffff 0,rgba(255,255,255,0) 100%),linear-gradient(180deg,#f0f2f4,#c7d0d9)"></div><span>Jon Dale</span></div>
  <div class="tm" style="left:978px;top:7170px"><div class="ph" role="img" aria-label="Team member portrait" style="background:radial-gradient(ellipse 40% 45% at 50% 78%,#2a7fd0 0,rgba(42,127,208,0) 100%),linear-gradient(180deg,#eef2f6,#cdd9e6)"></div><span>Ada Orin</span></div>
  <div class="tm" style="left:1330px;top:7170px"><div class="ph" role="img" aria-label="Team member portrait" style="background:radial-gradient(ellipse 35% 45% at 45% 75%,#ffffff 0,rgba(255,255,255,0) 100%),linear-gradient(90deg,#ece6da 0%,#d9d2c2 55%,#8fa76a 100%)"></div><span>Marcus Treval</span></div>
  <div class="btn" style="left:876px;top:7652px;font-size:15px;padding:12px 26px">View More</div>

  <!-- footer -->
  <footer class="footer">
    <div class="bar">Copyright © 2021 <b>WPQ Research Program</b>. All rights reserved.</div>
  </footer>
  <div class="partners">
    <i style="width:150px;height:34px"></i>
    <i style="width:60px;height:60px;border-radius:50%"></i>
    <i style="width:150px;height:34px"></i>
    <i style="width:110px;height:60px"></i>
    <i style="width:140px;height:34px"></i>
    <i style="width:60px;height:60px;border-radius:50%"></i>
  </div>
  <div class="fcol f-about">
    <div class="f-brand"><i></i><span>Wellness, Purpose, and the Quiet Path Research Program</span></div>
    Lorem ipsum dolor sit amet, consectetur adipiscing elit. Integer hendrerit tellus a nibh vehicula, ac gravida lorem pulvinar.
    <div class="soc"><i></i><i></i><i></i><i></i></div>
  </div>
  <div class="fcol" style="left:832px"><h6>Quick <b>Links</b></h6>Home<br>People<br>Projects<br>FAQ<br>Resource<br>Contact</div>
  <div class="fcol" style="left:1095px"><h6>Our <b>Projects</b></h6>Lorem ipsum dolor<br>Lorem ipsum dolor<br>Lorem ipsum dolor<br>Lorem ipsum dolor<br>Lorem ipsum dolor<br>Lorem ipsum dolor</div>
  <div class="fcol" style="left:1394px;width:260px"><h6>Contact <b>Us</b></h6>
    <div class="lab">Address</div><div class="val">Av. Lindera 418,<br>Santa Rosa</div>
    <div class="lab">Phone</div><div class="val">0147 - 258 - 369</div>
    <div class="lab">Email</div><div class="val">info@wpqp.org</div>
  </div>

</div>
</body>
</html>
```